Business Card Design

We need a new buisness card designed for a new company in Darwin
We dig trenchs and lay pipes for the communication industry,Electrical industry, Teleco industry,
We also do some concrete works as well,
And small excavation work
Communication
Belvanti Contracting PTY LTD
Pit and Pipe installations
Trenching,Excavations, Concreting ,
civil works, unistrut soloutions ,over thirty years experiance
NOTHING TOO DEEP WE WILL DIG ANYTHING
Contact Glen 0491536208 ps
(would like name to stand out somehow in another text or graphic sort of a way am also looking for some sort of slogan) will most likely be a red card with black writing

```html
<!DOCTYPE html>
<html lang="en">
<head>
<meta charset="utf-8">
<title>Belvanti Contracting PTY LTD – Business Card</title>
<link rel="stylesheet" href="https://fonts.googleapis.com/css2?family=Lexend:wght@700;800&display=swap">
<style>
  :root {
    --card-red: #c9212b;
    --brand-yellow: #fbef2a;
    --detail-tan: #eab55e;
    --contact-white: #ffffff;
  }
  html, body {
    margin: 0;
    padding: 0;
    width: 1200px;
    height: 741px;
    overflow: hidden;
    background: var(--card-red);
  }
  .card {
    display: block;
    width: 1200px;
    height: 741px;
    background: var(--card-red);
  }
  .card text {
    font-family: "Lexend", "Arial Black", sans-serif;
    font-weight: 800;
    text-anchor: middle;
  }
  .brand-name { font-size: 104px; fill: var(--brand-yellow); }
  .brand-suffix { font-size: 58px; fill: var(--brand-yellow); }
  .experience { font-size: 31px; font-weight: 700; fill: var(--detail-tan); }
  .services { font-size: 30px; font-weight: 700; fill: var(--detail-tan); }
  .contact-name { font-size: 90px; fill: var(--contact-white); }
  .contact-phone { font-size: 100px; fill: var(--contact-white); }
  .slogan { font-size: 45px; fill: var(--brand-yellow); }
</style>
</head>
<body>
  <svg class="card" viewBox="0 0 1200 741" role="group" aria-label="Belvanti Contracting PTY LTD business card">
    <rect class="card__background" width="1200" height="741" fill="var(--card-red)"/>
    <text class="brand-name" x="600" y="128" textLength="652" lengthAdjust="spacingAndGlyphs">BELVANTI</text>
    <text class="brand-suffix" x="600" y="191" textLength="650" lengthAdjust="spacingAndGlyphs">Contracting PTY LTD</text>
    <text class="experience" x="600" y="264" textLength="451" lengthAdjust="spacingAndGlyphs">Over 30 years experience</text>
    <text class="services" x="609" y="319" textLength="793" lengthAdjust="spacingAndGlyphs">• TRENCHING  • EXCAVATIONS  • CONCRETING</text>
    <text class="services" x="609" y="356" textLength="802" lengthAdjust="spacingAndGlyphs">• PIT AND PIPE INSTALLATIONS  • CIVIL WORKS</text>
    <text class="contact-name" x="600" y="489" textLength="267" lengthAdjust="spacingAndGlyphs">Glen</text>
    <text class="contact-phone" x="606" y="598" textLength="632" lengthAdjust="spacingAndGlyphs">0491536208</text>
    <text class="slogan" x="601" y="678" textLength="1090" lengthAdjust="spacingAndGlyphs">NOTHING TOO DEEP WE WILL DIG ANYTHING</text>
  </svg>
</body>
</html>
```